Danke für den tollen Flyer und die nette Zusammenarbeit. Gerne wieder.
Zielgruppe
Ich betreibe eine mobile Hundeschule / Hundetraining. Meine Zielgruppe sind Hundehalter:innen, junge Menschen und jung Gebliebene.
Aufgabenstellung
Das Design soll in erster Linie modern sein, aber auch kompetent und sympathisch wirken. Texte würde ich gerne in Absprache mit dem Designer erstellen.
Ich wünsche mir einen Faltflyer in Standardgröße (ich glaube das heißt DIN lang, 2 mal gefaltet (Wickelfalz), 99x210mm.
IM AMHANG SIND BILDER DER NEUEN HOMEPAGE. DIESE IST NCOH NICHT ONLINE. DAS DESIGN SOLL SICH GERNE AN DEN BILDERN DER HOMEPAGE ORIENTIEREN.

```html
<!DOCTYPE html>
<html lang="de">
<head>
<meta charset="utf-8">
<title>Pfotenschule Emsland – Faltflyer</title>
<link href="https://fonts.googleapis.com/css2?family=Roboto+Slab:wght@300;400;700&family=Caveat:wght@500&display=swap" rel="stylesheet">
<style>
  :root{
    --brown:#4d2e1b;
    --brown-dark:#3a2213;
    --gold:#e3a53a;
    --paper:#f4f2ef;
    --white:#ffffff;
    --ink:#2b2b2b;
    --muted:#6d6660;
    --stage:#e4e2df;
  }
  *{box-sizing:border-box;margin:0;padding:0}
  html,body{width:1200px;height:1200px;overflow:hidden}
  body{background:var(--stage);font-family:"Roboto Slab",Georgia,serif;color:var(--ink)}
  .sheet{position:absolute;left:200px;width:800px;height:566px;background:var(--paper);overflow:hidden;box-shadow:0 6px 18px rgba(0,0,0,.18)}
  .sheet--inside{top:24px}
  .sheet--outside{top:610px}
  .photo{position:absolute}
  .abs{position:absolute}

  /* inside */
  .hero-band{left:0;top:0;width:800px;height:175px;background:linear-gradient(180deg,#e8dccb 0%,#cfb393 55%,#b58c63 100%)}
  .hero-fade{left:0;top:120px;width:800px;height:70px;background:linear-gradient(180deg,rgba(244,242,239,0),var(--paper))}
  .badge{left:292px;top:8px;width:136px;height:136px;border-radius:50%;background:var(--white);display:flex;align-items:center;justify-content:center;padding:16px;box-shadow:0 2px 6px rgba(0,0,0,.15)}
  .badge-text{font-size:8.5px;font-weight:700;line-height:1.4;text-align:center;width:100%}
  .badge-text em{font-style:normal;color:var(--gold)}
  .hours-tag{left:600px;top:22px;width:150px;background:var(--white);padding:9px 12px;box-shadow:0 2px 6px rgba(0,0,0,.12)}
  .hours-tag h3{font-size:12px;font-weight:700}
  .hours-tag p{font-size:9px;margin-top:2px}
  .section-title{left:40px;top:196px;font-size:17px;font-weight:700;letter-spacing:.08em;line-height:1.2;color:var(--brown)}
  .brown-base{left:0;top:300px;width:800px;height:266px;background:var(--brown)}
  .offer{position:absolute;width:220px}
  .offer .photo{position:relative;width:220px;height:120px}
  .offer-card{background:var(--white);padding:14px 16px 16px;box-shadow:0 3px 8px rgba(0,0,0,.2)}
  .offer-card h3{font-size:17px;font-weight:700;color:var(--ink);padding-bottom:6px;border-bottom:2px solid var(--gold);display:inline-block}
  .offer-card .kicker{font-size:9px;color:var(--muted);margin-top:7px}
  .offer-card p{font-size:9.5px;line-height:1.45;margin-top:8px}
  .offer-card small{display:block;font-size:8px;color:var(--muted);margin-top:8px}

  /* outside */
  .col-left{left:0;top:0;width:267px;height:566px;background:var(--paper)}
  .portrait{left:0;top:0;width:267px;height:300px;background:linear-gradient(160deg,#d9d9d9,#9a9a9a 60%,#c8c8c8)}
  .intro{left:22px;top:322px;width:230px}
  .intro h2{font-size:19px;font-weight:700;line-height:1.3}
  .intro .lead{font-size:10.5px;margin-top:10px;line-height:1.4}
  .intro p.body{font-size:8.5px;line-height:1.55;color:var(--muted);margin-top:12px}
  .col-mid-top{left:267px;top:0;width:267px;height:350px;background:var(--brown)}
  .col-mid-bottom{left:267px;top:350px;width:267px;height:216px;background:var(--paper)}
  .placeholder{left:290px;top:22px;font-size:9px;color:#d9c6b4}
  .field-photo{left:205px;top:95px;width:230px;height:235px;background:linear-gradient(180deg,#7d8a5c 0%,#a39a62 45%,#c7a86a 100%);box-shadow:0 3px 8px rgba(0,0,0,.25)}
  .info-box{position:absolute;left:378px;width:146px;background:var(--white);padding:10px 12px;box-shadow:0 3px 8px rgba(0,0,0,.22)}
  .info-box h3{font-size:13px;font-weight:700}
  .info-box p{font-size:9.5px;margin-top:3px}
  .info-box small{display:block;font-size:7.5px;color:var(--muted);margin-top:4px}
  .contact{left:267px;top:382px;width:267px;text-align:center}
  .contact .dot{width:40px;height:40px;border-radius:50%;background:var(--brown);margin:0 auto 14px}
  .contact p{font-size:9.5px;line-height:1.6}
  .cover{left:534px;top:0;width:266px;height:430px;background:linear-gradient(180deg,#7b6a58 0%,#8c6c4d 40%,#b3784a 75%,#6e5a45 100%)}
  .cover-text{left:560px;top:22px;width:220px;text-align:center}
  .cover-text h1{font-size:17px;font-weight:400;line-height:1.35;color:var(--white)}
  .cover-text h1 span{color:var(--gold)}
  .cover-text .script{font-family:"Caveat",cursive;font-size:22px;color:var(--white);margin-top:10px}
  .brand{left:534px;top:430px;width:266px;height:136px;background:var(--white);display:flex;align-items:center;justify-content:center;gap:12px}
  .brand .mark{width:34px;height:34px;border-radius:50%;background:var(--gold);flex:none}
  .brand .name{font-size:17px;font-weight:700;color:var(--brown);line-height:1.15}
</style>
</head>
<body>

<section class="sheet sheet--inside">
  <div class="photo abs hero-band" role="img" aria-label="Hund auf herbstlicher Wiese, unscharfer Hintergrund"></div>
  <div class="abs hero-fade"></div>
  <div class="abs badge"><p class="badge-text">Hundeschule &amp; Verhaltensberatung mit Basis <em>positiver</em> Verstärkung</p></div>
  <div class="abs hours-tag"><h3>Trainingszeiten</h3><p>Täglich: 09:00 – 19:00</p></div>
  <h2 class="abs section-title">VIELFÄLTIGE<br>TRAININGSANGEBOTE</h2>
  <div class="abs brown-base"></div>

  <article class="offer" style="left:40px;top:255px">
    <div class="photo" role="img" aria-label="Hund beim Einzeltraining im Wald" style="background:linear-gradient(160deg,#6f5334,#b78a55 60%,#5c4126)"></div>
    <div class="offer-card">
      <h3>Einzeltraining</h3>
      <div class="kicker">1:1 Coaching</div>
      <p>Optimal für Probleme oder sehr individuelle Themen</p>
      <small>Für Welpen, Junghunde und erwachsene Hunde</small>
    </div>
  </article>

  <article class="offer" style="left:290px;top:222px">
    <div class="photo" role="img" aria-label="Gruppe von Hunden beim gemeinsamen Training" style="background:linear-gradient(160deg,#4f5d3a,#8a8459 55%,#6b5a3c)"></div>
    <div class="offer-card">
      <h3>Gruppentraining</h3>
      <div class="kicker">Spaß in der Gruppe</div>
      <p>Optimal für Alltagstraining und Beschäftigung</p>
      <small>Für Welpen, Junghunde und erwachsene Hunde</small>
    </div>
  </article>

  <article class="offer" style="left:540px;top:150px">
    <div class="photo" role="img" aria-label="Hundehalterin mit Hund bei einem Workshop im Wald" style="background:linear-gradient(160deg,#3f4a30,#6d6a45 50%,#9c7a4d)"></div>
    <div class="offer-card">
      <h3>Workshops</h3>
      <div class="kicker">Spezielle Themen</div>
      <p>Optimal für effektives Training in kurzer Zeit</p>
      <small>Termine nach Absprache</small>
    </div>
  </article>
</section>

<section class="sheet sheet--outside">
  <div class="abs col-left"></div>
  <div class="photo abs portrait" role="img" aria-label="Schwarzweißfoto der Hundetrainerin im Freien"></div>
  <div class="abs intro">
    <h2>Entspannter und glücklicher im Alltag mit Hund</h2>
    <p class="lead">Fundiertes Training, Beratung und Wissensvermittlung</p>
    <p class="body">Gemeinsam mit Ihnen entwickle ich ein Training, das zu Ihrem Hund und Ihrem Alltag passt. Freundlich, verständlich und auf Basis positiver Verstärkung – mobil bei Ihnen vor Ort.</p>
  </div>

  <div class="abs col-mid-top"></div>
  <div class="abs col-mid-bottom"></div>
  <div class="abs placeholder">Platz für Text</div>
  <div class="photo abs field-photo" role="img" aria-label="Trainerin kniet auf einer Wiese, ein Hund läuft auf sie zu"></div>
  <div class="info-box" style="top:112px"><h3>Trainingszeiten</h3><p>Täglich: 09:00 – 19:00</p><small>Termine nach Vereinbarung</small></div>
  <div class="info-box" style="top:205px"><h3>Schnellkontakt</h3><p>Tel.: 0151 / 204 77 31 8</p><small>Rufen Sie mich gerne an</small></div>
  <div class="abs contact">
    <div class="dot"></div>
    <p>0934 / 608 21 47 3<br>info@pfotenschule-ems.de<br>www.pfotenschule-ems.de</p>
  </div>

  <div class="photo abs cover" role="img" aria-label="Rotbrauner Hund mit offenem Maul vor herbstlichem Hintergrund"></div>
  <div class="abs cover-text">
    <h1>Hundeschule &amp;<br><span>Verhaltensberatung</span><br>mit Basis positiver<br>Verstärkung</h1>
    <div class="script">Erreichen Sie mich!</div>
  </div>
  <div class="abs brand">
    <div class="mark"></div>
    <div class="name">PFOTENSCHULE<br>EMSLAND</div>
  </div>
</section>

</body>
</html>
```